Pinecrest Real Estate A5 Flyer

A5 Flyer for print distribution.

Front (include attached photo and branding):
Pinecrest are a new face in the Shelley & Rossmoyne real estate market. The Pinecrest team are both Shelley ‘locals’ and are genuinely and sincerely committed to this community. They put people first and pursue exceptional outcomes for their clients. This is the founding vision of Pinecrest.

Values:
Outstanding Customer Service
Timely Communication
Integrity Always
People First
Exceptional Negotiation

If you’re thinking of selling, interested in a free market appraisal, or simply want to find out more about the Pinecrest team, please reach out to Doug or Rowan for a chat. We’d love to shout you a coffee at The Lantern Coffee + Kitchen.

Pinecrest Real Estate
E: hello@pinecrestrealestate-example.com.au
W: pinecrestrealestate-example.com.au

Back (half the page about Doug, other half the page about Rowan). Please include headshots (Rowan is the younger one):

Rowan Ferrabee (Property Consultant):

Rowan has an in-depth understanding of all things property & finance related. With a degree in property & finance, diploma in finance & mortgage broking, certificate IV in real estate practice, project management roles in residential property development, plus years of small business experience as co-founder/co-owner of The Lantern Coffee + Kitchen, his experience in managing competing demands and complex scenarios runs far and wide.

Rowan also has experience in corporate negotiations which is proving to be a very beneficial skill set. Rowan is deeply committed to people and pursuing exceptional outcomes for his clients. He has built a reputation as a man of his word who is genuine and sincere and willing to go above and beyond for his clients.

rowan@pinecrestrealestate-example.com.au
0412 306 248

Doug Penberthy (Director / Licensee):

Doug has worked in various roles inclusive of being a Real Estate Agent, Bank Manager, Financial Counsellor, Mortgage Broker, and previously a Commercial Pilot. He spent eight years in remote Western Australia, where he worked for an international mining company creating strategies to help support the well-being of employees. Doug’s focus in life has always been to help people. To him, it is always about the relationship. Doug gets enormous satisfaction from seeing individuals, families, and businesses thrive financially. He has become a skilled negotiator with extensive experience working for a number of corporations and private firms.
 
What differentiates Doug is his compassion and commitment to people. He works hard to be an excellent communicator with the aim of achieving great results. He  has extensive sales experience with incredible ability to push the boundaries, think outside the box and meet or surpass expectations. This is why his clients keep coming back and continue to refer well into the future. 

doug@pinecrestrealestate-example.com.au
0438 192 607

Target Market(s)

House Sellers / House Buyers

Industry/Entity Type

Real Estate

Colors
0054AA
0677BA
7BADD7
CADEEF
E8F1F8

Requirements
Must have
• Branding / logo, river photo, head shots, company details etc
Nice to have
• Design as per attached branding guide

```html
<!DOCTYPE html>
<html lang="en">
<head>
<meta charset="utf-8">
<title>Pinecrest Real Estate – A5 Flyer</title>
<link href="https://fonts.googleapis.com/css2?family=Rubik:wght@300;400;500&display=swap" rel="stylesheet">
<style>
:root{
  --navy:#101c2c;
  --slate:#7b8199;
  --slate-light:#c9ccd6;
  --panel-grey:#e4e5ea;
  --ink:#1d2230;
  --paper:#ffffff;
  --canvas:#e9e9eb;
  --water:#5f7e96;
  --land:#6e7a5a;
}
*{box-sizing:border-box;margin:0;padding:0}
html,body{width:1050px;height:1200px;overflow:hidden}
body{background:var(--canvas);font-family:"Rubik",sans-serif;color:var(--ink);position:relative}
.page{position:absolute;top:246px;width:500px;height:707px;background:var(--paper);overflow:hidden;box-shadow:0 4px 14px rgba(0,0,0,.18)}
.front{left:15px}
.back{left:535px;background:linear-gradient(90deg,#eef0f3 0%,#fff 18%,#fff 100%)}

/* wordmark */
.wordmark{display:flex;align-items:center;gap:12px;position:absolute}
.wordmark-dot{width:36px;height:36px;border-radius:50%;background:var(--navy)}
.wordmark-name{font-family:"Rubik",sans-serif;font-weight:400;color:var(--navy);letter-spacing:.32em;font-size:24px}
.front .wordmark{top:22px;left:0;right:0;justify-content:center}

/* front hero */
.hero{position:absolute;top:80px;left:0;width:500px;height:240px}
.intro{position:absolute;left:28px;top:337px;width:245px;font-size:11px;line-height:15.5px;font-weight:400}
.intro p{margin-bottom:15px}
.values{position:absolute;left:303px;top:300px;width:197px;height:232px;background:var(--navy);border-bottom-left-radius:28px;padding:42px 12px 0 12px;color:#fff}
.values h2{font-weight:400;font-size:19px;color:var(--slate-light);margin-bottom:10px}
.values ul{list-style:none;font-size:10.5px;line-height:14px;font-weight:300}
.values li{position:relative;padding-left:18px;margin-bottom:9px}
.values li::before{content:"•";position:absolute;left:6px}
.cta{position:absolute;left:51px;top:545px;width:398px;height:93px;border:1px solid var(--slate-light);padding:5px}
.cta-inner{background:var(--panel-grey);height:100%;text-align:center;font-size:10.4px;line-height:14px;padding:8px 12px;font-weight:300}
.cta-inner .accent{color:var(--slate)}
.cta-inner b{font-weight:500}
.cta-inner p+p{margin-top:6px}
.footer-band{position:absolute;left:0;bottom:0;width:365px;height:46px;background:var(--slate);border-top-right-radius:16px;color:#fff;padding:8px 0 0 28px;font-size:8.2px;line-height:12px;font-weight:300}
.footer-band strong{font-weight:500;font-size:9px;display:block}
.footer-mark{position:absolute;right:24px;bottom:8px;display:flex;flex-direction:column;align-items:center;gap:5px}
.footer-mark .wordmark-dot{width:22px;height:22px}
.footer-mark span{font-size:7px;letter-spacing:.3em;color:var(--navy)}

/* back */
.bio{position:absolute;top:22px;width:215px}
.bio-rowan{left:20px}
.bio-doug{left:270px}
.headshot{position:absolute;top:0;right:0;width:66px;height:66px;border-radius:50%;border:3px solid #fff;box-shadow:0 1px 4px rgba(0,0,0,.25);background:radial-gradient(circle at 50% 40%,#d9d3cc 0%,#b8b3ae 55%,#2d3a55 100%)}
.bio h3{margin-top:32px;font-weight:500;font-size:15px;color:var(--ink)}
.bio .role{font-size:11px;font-weight:300;margin-bottom:12px}
.bio p{font-size:9.6px;line-height:14.2px;font-weight:300;margin-bottom:14px}
.bio .email{font-size:9.4px;margin-top:-2px}
.bio .phone{font-size:13.5px;font-weight:500;margin-top:4px}
.back-photo{position:absolute;left:0;bottom:0;width:155px;height:180px;border-top-right-radius:16px;background:linear-gradient(180deg,#d7dde3 0%,#9fb0bd 30%,#54697b 55%,#6a7758 75%,#4e5e4a 100%)}
.back .wordmark{right:42px;bottom:28px}
.back .wordmark-dot{width:30px;height:30px}
.back .wordmark-name{font-size:18px}
</style>
</head>
<body>

<section class="page front">
  <div class="wordmark"><span class="wordmark-dot"></span><span class="wordmark-name">PINECREST</span></div>

  <svg class="hero" viewBox="0 0 500 240" role="img" aria-label="Aerial photograph of the Shelley riverfront and suburb">
    <defs>
      <linearGradient id="heroFill" x1="0" y1="0" x2="1" y2="1">
        <stop offset="0" stop-color="#b9c6cf"/>
        <stop offset=".35" stop-color="#6f8aa0"/>
        <stop offset=".6" stop-color="#6e7a5a"/>
        <stop offset="1" stop-color="#8a8b86"/>
      </linearGradient>
      <linearGradient id="swoosh" x1="0" y1="0" x2="1" y2="0">
        <stop offset="0" stop-color="#eceef2"/>
        <stop offset=".6" stop-color="#b9bdc9"/>
        <stop offset="1" stop-color="#7b8199"/>
      </linearGradient>
    </defs>
    <path d="M0 240 L0 70 C80 160 230 215 380 180 C440 165 480 145 500 130 L500 240 Z" fill="url(#swoosh)"/>
    <path d="M0 0 H500 V120 C470 145 430 165 380 172 C230 200 80 150 0 62 Z" fill="url(#heroFill)"/>
  </svg>

  <div class="intro">
    <p>Pinecrest are a new face in the Shelley &amp; Rossmoyne real estate market. The Pinecrest team are both Shelley ‘locals’ and are genuinely and sincerely committed to this community.</p>
    <p>They put people first and pursue exceptional outcomes for their clients.</p>
    <p>This is the founding vision of Pinecrest.</p>
  </div>

  <aside class="values">
    <h2>Values:</h2>
    <ul>
      <li>Outstanding Customer Service</li>
      <li>Timely Communication</li>
      <li>Integrity Always</li>
      <li>People First</li>
      <li>Exceptional Negotiation</li>
    </ul>
  </aside>

  <div class="cta"><div class="cta-inner">
    <p>If you’re thinking of selling, interested in a free market appraisal, or simply want to find out more about the <span class="accent">Pinecrest team</span>, please reach out to <b>DOUG</b> or <b>ROWAN</b> for a chat.</p>
    <p>We’d love to shout you a coffee at The Lantern Coffee + Kitchen.</p>
  </div></div>

  <footer class="footer-band">
    <strong>Pinecrest Real Estate</strong>
    E: hello@pinecrestrealestate-example.com.au &nbsp;|&nbsp; W: pinecrestrealestate-example.com.au
  </footer>
  <div class="footer-mark"><span class="wordmark-dot"></span><span>PINECREST</span></div>
</section>

<section class="page back">
  <article class="bio bio-rowan">
    <div class="headshot" role="img" aria-label="Headshot of Rowan Ferrabee"></div>
    <h3>Rowan Ferrabee</h3>
    <div class="role">(Property Consultant):</div>
    <p>Rowan has an in-depth understanding of all things property &amp; finance related. With a degree in property &amp; finance, diploma in finance &amp; mortgage broking, certificate IV in real estate practice, project management roles in residential property development, plus years of small business experience as co-founder/co-owner of The Lantern Coffee + Kitchen, his experience in managing competing demands and complex scenarios runs far and wide.</p>
    <p>Rowan also has experience in corporate negotiations which is proving to be a very beneficial skill set. Rowan is deeply committed to people and pursuing exceptional outcomes for his clients. He has built a reputation as a man of his word who is genuine and sincere and willing to go above and beyond for his clients.</p>
    <div class="email">rowan@pinecrestrealestate-example.com.au</div>
    <div class="phone">0412 306 248</div>
  </article>

  <article class="bio bio-doug">
    <div class="headshot" role="img" aria-label="Headshot of Doug Penberthy"></div>
    <h3>Doug Penberthy</h3>
    <div class="role">(Director / Licensee):</div>
    <p>Doug has worked in various roles inclusive of being a Real Estate Agent, Bank Manager, Financial Counsellor, Mortgage Broker, and previously a Commercial Pilot. He spent eight years in remote Western Australia, where he worked for an international mining company creating strategies to help support the well-being of employees. Doug’s focus in life has always been to help people. To him, it is always about the relationship. Doug gets enormous satisfaction from seeing individuals, families, and businesses thrive financially. He has become a skilled negotiator with extensive experience working for a number of corporations and private firms.</p>
    <p>What differentiates Doug is his compassion and commitment to people. He works hard to be an excellent communicator with the aim of achieving great results. He has extensive sales experience with incredible ability to push the boundaries, think outside the box and meet or surpass expectations. This is why his clients keep coming back and continue to refer well into the future.</p>
    <div class="email">doug@pinecrestrealestate-example.com.au</div>
    <div class="phone">0438 192 607</div>
  </article>

  <div class="back-photo" role="img" aria-label="Aerial photograph of the river bend and suburb"></div>
  <div class="wordmark"><span class="wordmark-dot"></span><span class="wordmark-name">PINECREST</span></div>
</section>

</body>
</html>
```